Brightwell Wiring Needs A Logo Design

We need a logo for my new company based out of Sacramento, Ca called Brightwell Wiring. The name says it all, my electrical contracting business provides "Brightwell Craftsman Work" I'm open to any colors that pop and customers to say Wow. I would love to print my cards on metal.

Contact Information for Business Card

The card needs to have as follows
Name of company: Brightwell Wiring
My Name: Marco Delvane
Phone # 916-555-0147
CL# 4873920
Email: brightwellwiring@mailtorva.com
and a slogan that represent "BRIGHTWELL"

Requirements
Must have
• The card needs to have as follows
• Name of company: Brightwell Wiring
• My Name : Marco Delvane
• Phone # 916-555-0147
• CL# 4873920
• Email: brightwellwiring@mailtorva.com
• and a slogan that represent "BRIGHTWELL"
Nice to have
• popping colors
• electrical Arcing

```html
<!DOCTYPE html>
<html lang="en">
<head>
<meta charset="utf-8">
<title>Brightwell Wiring – Business Card</title>
<link rel="stylesheet" href="https://fonts.googleapis.com/css2?family=Open+Sans:wght@400;600;700&display=swap">
<style>
  :root {
    --teal: #0b86a8;
    --orange: #ef930c;
    --white: #ffffff;
    --backdrop: #e9e6e2;
    --ink-light: #ffffff;
  }
  * { margin: 0; padding: 0; box-sizing: border-box; }
  html, body {
    width: 1200px; height: 900px; overflow: hidden;
    background: var(--backdrop);
    font-family: "Open Sans", Arial, sans-serif;
  }
  .canvas { position: relative; width: 1200px; height: 900px; }

  .card { position: absolute; overflow: hidden; box-shadow: 0 6px 18px rgba(0,0,0,.18); }

  /* Front */
  .card-front { left: 78px; top: 35px; width: 588px; height: 363px; background: var(--white); }
  .card-front .bands { position: absolute; inset: 0; }
  .brand {
    position: absolute; left: 0; right: 0; top: 78px;
    display: flex; align-items: center; justify-content: center; gap: 16px;
  }
  .brand-mark { width: 34px; height: 34px; background: var(--teal); }
  .brand-name { font-size: 38px; font-weight: 600; color: var(--teal); letter-spacing: .5px; }

  .contact-list {
    position: absolute; right: 270px; top: 253px;
    list-style: none; text-align: right; color: var(--ink-light); font-size: 15px;
  }
  .contact-list li { display: flex; justify-content: flex-end; align-items: center; gap: 8px; height: 25px; }
  .contact-list svg { width: 12px; height: 12px; fill: var(--ink-light); }
  .holder-name {
    position: absolute; left: 343px; top: 274px;
    font-size: 20px; font-weight: 700; color: var(--ink-light);
  }

  /* Back */
  .card-back {
    left: 388px; top: 505px; width: 566px; height: 352px; background: var(--teal);
    display: flex; align-items: center; justify-content: center;
  }
  .back-name { font-size: 40px; font-weight: 600; color: var(--white); letter-spacing: 1px; }
</style>
</head>
<body>
<div class="canvas">

  <section class="card card-front">
    <svg class="bands" viewBox="0 0 588 363" width="588" height="363" aria-hidden="true">
      <polygon points="0,198 402,198 381,225 0,225" fill="var(--orange)"/>
      <polygon points="414,190 588,190 588,363 0,363 0,227 386,227" fill="var(--teal)"/>
    </svg>

    <div class="brand">
      <span class="brand-mark"></span>
      <span class="brand-name">Brightwell Wiring</span>
    </div>

    <ul class="contact-list">
      <li>916-555-0147
        <svg viewBox="0 0 24 24"><path d="M6.6 10.8a15 15 0 0 0 6.6 6.6l2.2-2.2c.3-.3.7-.4 1-.2 1.1.4 2.3.6 3.6.6.6 0 1 .4 1 1V20c0 .6-.4 1-1 1A17 17 0 0 1 3 4c0-.6.4-1 1-1h3.5c.6 0 1 .4 1 1 0 1.3.2 2.5.6 3.6.1.3 0 .7-.2 1z"/></svg>
      </li>
      <li>4873920
        <svg viewBox="0 0 24 24"><path d="M7 1h10a2 2 0 0 1 2 2v18a2 2 0 0 1-2 2H7a2 2 0 0 1-2-2V3a2 2 0 0 1 2-2zm0 3v14h10V4zm5 15.5a1 1 0 1 0 0 2 1 1 0 0 0 0-2z"/></svg>
      </li>
      <li>brightwellwiring@mailtorva.com
        <svg viewBox="0 0 24 24"><path d="M2 5h20v14H2zm2 2v.5l8 5 8-5V7zm0 2.8V17h16V9.8l-8 5z"/></svg>
      </li>
    </ul>
    <p class="holder-name">Marco Delvane</p>
  </section>

  <section class="card card-back">
    <p class="back-name">Brightwell Wiring</p>
  </section>

</div>
</body>
</html>
```